Bright Valley Goods - Product Page

Looking for a design for our product pages to showcase all of the following information in an aesthetically pleasing way. <br/><br/>• Product price per piece & price breaks<br/>• Set up cost <br/>• Additional color cost<br/>• Imprint side <br/>• Product Dimensions<br/><br/>Attached are photos showing ideas we have come up with to display the information. <br/><br/>The link below shows how our product pages is currently laid out. <br/><br/>Link to webpage: https://www.brightvalleygoods.example/non-woven-reusable-promo-totes.html<br/>

Number of Pages Required

1 page

Colors
33b8a4
33a6d7
3277b5
fece3e
f9a040
a3cd3a

Requirements
Must have
• • Product price per piece & price breaks
• • Set up cost
• • Additional color cost
• • Imprint side
• • Product Dimensions

```html
<!DOCTYPE html>
<html lang="en">
<head>
<meta charset="utf-8">
<title>Bright Valley Goods – Product Page</title>
<link href="https://fonts.googleapis.com/css2?family=Montserrat:wght@400;500;600;700&family=Varela+Round&display=swap" rel="stylesheet">
<style>
:root{
  --navy:#0d3b66;
  --navy-dark:#0a2f52;
  --green:#4aa52c;
  --green-light:#5cbf2a;
  --green-deep:#3a9420;
  --red:#e0262b;
  --orange:#f9a040;
  --ink:#222;
  --muted:#666;
  --line:#dcdcdc;
  --hero-bg:#ebebeb;
}
*{box-sizing:border-box;margin:0;padding:0}
html,body{width:1200px;height:3838px;overflow:hidden}
body{position:relative;font-family:"Montserrat",sans-serif;color:var(--ink);background:#fff}
.abs{position:absolute}
.display{font-family:"Varela Round",sans-serif}

/* header */
.brand{left:89px;top:38px;font-family:"Montserrat",sans-serif;font-weight:700;font-size:30px;color:var(--green);line-height:1}
.brand small{display:block;font-size:17px;margin-top:6px;color:var(--green)}
.search{left:411px;top:39px;width:325px;height:56px;border:2px solid #e3e3e3;border-radius:28px;font-size:16px;color:#555;padding:17px 0 0 24px}
.search-btn{right:8px;top:8px;width:38px;height:38px;border-radius:50%;background:var(--green)}
.cart{left:782px;top:52px;font-size:17px;color:#444;display:flex;align-items:flex-end;gap:4px}
.phone-ico{left:886px;top:42px;width:48px;height:48px;border-radius:50%;background:var(--green)}
.phone-txt{left:954px;top:44px;font-size:15px;color:#444;line-height:1.6}
.phone-txt b{font-weight:500;font-size:17px;color:#222;letter-spacing:.5px}

.nav{left:0;top:131px;width:1200px;height:65px;background:var(--navy)}
.nav a{position:absolute;top:20px;color:#fff;text-decoration:none;font-size:20px}
.nav a.active{color:var(--green-light)}

/* hero */
.hero{left:0;top:196px;width:1200px;height:522px;background:linear-gradient(90deg,#f2f2f2,#e6e6e6 60%,#efefef)}
.hero-photo{left:507px;top:20px;width:343px;height:502px;background:linear-gradient(180deg,#d9cbbb,#a89077 55%,#5f6d80);border-radius:120px 120px 0 0;opacity:.85}
.hero-title{top:180px;font-size:62px;letter-spacing:1px}
.rush{left:1015px;top:258px;width:80px;height:80px;border-radius:50%;background:var(--red);border:3px solid #fff;box-shadow:0 3px 8px rgba(0,0,0,.25);color:#fff;text-align:center;font-weight:700;font-size:14px;line-height:1;padding-top:17px}
.rush span{display:block;font-size:8px;margin-top:4px;font-weight:600}
.dot{width:10px;height:10px;border-radius:50%}

/* recommended */
.sec-title{left:0;width:1200px;text-align:center;font-size:27px}
.card{top:942px;width:237px;height:323px;background:#fff;box-shadow:0 0 6px rgba(0,0,0,.18);overflow:hidden}
.card .img{left:30px;top:12px;width:177px;height:156px;border-radius:6px}
.card .stars{left:12px;top:173px;color:var(--orange);font-size:15px;letter-spacing:2px}
.card .name{left:12px;top:202px;font-size:14px;color:#333}
.card .price{right:14px;top:200px;font-size:15px;font-weight:600;color:var(--red)}
.card .size{left:12px;top:245px;font-size:12px;color:#333;width:213px}
.card .size span{float:right;font-size:11px}
.card .cta{left:10px;top:278px;height:30px;padding:0 12px;border:1px solid #ccc;border-radius:15px;font-size:12px;line-height:28px;color:#333}
.card .cta.on{background:var(--navy);color:#fff;border-color:var(--navy)}
.card .ico{top:278px;width:30px;height:30px;border-radius:50%;background:#eee}
.ribbon{right:-30px;top:10px;width:120px;transform:rotate(0);background:var(--green-light);color:#fff;font-size:13px;text-align:center;padding:4px 0}
.sale{left:-34px;top:14px;width:110px;transform:rotate(-45deg);background:var(--green-light);color:#fff;font-size:13px;text-align:center;padding:4px 0}

/* banner */
.banner{left:0;top:1456px;width:1200px;height:484px;background:linear-gradient(90deg,#b9a4a2,#c8b4b2 40%,#cdbbb8)}
.banner-person{left:200px;top:0;width:340px;height:484px;background:linear-gradient(180deg,#8a6a60,#3e4d66 40%,#e6e2d4 60%,#d9a9b3);opacity:.8;border-radius:60px}
.banner h2{left:524px;top:1570px;font-size:52px;font-weight:400}
.banner-copy{left:534px;top:1652px;width:560px;font-size:18px;line-height:34px;color:#222;font-weight:500}
.btn-shop{left:534px;top:1779px;width:198px;height:54px;border-radius:27px;background:var(--green);color:#fff;font-size:19px;font-weight:600;text-align:center;line-height:54px}

/* product detail */
.gallery{left:98px;top:2022px;width:468px;height:440px;border:1px solid #ddd;box-shadow:0 0 6px rgba(0,0,0,.12)}
.thumb{width:78px;height:76px;border:1px solid #8aa0bb}
.thumb i{position:absolute;left:14px;top:8px;width:48px;height:58px;border-radius:4px}
.main-img{left:201px;top:2086px;width:256px;height:285px;background:linear-gradient(90deg,#c8222b 0 48%,#b69a6c 52%);border-radius:6px}
.vline{top:2090px;width:1px;height:280px;background:#ddd}
.size-line{left:265px;top:2412px;font-size:20px;color:#333}
.size-line b{font-weight:500;color:var(--navy);margin-left:16px}
.sku{left:642px;top:2018px;font-size:26px;font-weight:500}
.review{left:642px;top:2062px;font-size:13px;color:#555}
.review span{color:var(--green);font-size:17px;letter-spacing:2px}

.ptable{left:642px;width:468px;border:1px solid #ddd}
.ptable .head{background:var(--navy);color:#fff;font-size:16px;height:36px;line-height:36px;padding-left:25px}
.ptable .row{display:grid;grid-template-columns:60px repeat(7,1fr);font-size:13px;color:#666;height:41px;line-height:41px;padding-left:12px;border-top:1px solid #e4e4e4}
.ptable .row:first-of-type{border-top:0}
.pbtn{top:2406px;height:38px;border-radius:19px;color:#fff;font-size:13px;text-align:center;line-height:38px}

/* production */
.prod{top:2527px;width:474px;height:396px;background:#fff;box-shadow:0 0 6px rgba(0,0,0,.15)}
.prod .head{height:82px;background:var(--navy);color:#fff;text-align:center;padding-top:14px;font-size:24px}
.prod .head small{display:block;font-size:19px;margin-top:6px}
.prod .line{left:30px;width:412px;font-size:21px;color:#333;border-bottom:1px solid #ddd;height:54px;padding-top:14px}
.prod .line span{position:absolute;left:297px;color:var(--navy)}
.prod .line:last-of-type{border-bottom:0}
.prod .foot{left:4px;bottom:2px;width:466px;height:60px;background:var(--green);color:#fff;font-size:23px;text-align:center;line-height:60px}

/* reviews */
.reviews{left:0;top:3008px;width:1200px;height:501px;background:linear-gradient(90deg,#3c9b20,#4cae28 50%,#5cbd2c)}
.reviews h2{left:0;width:1200px;top:3086px;text-align:center;color:#fff;font-size:44px;font-weight:400}
.rcard{top:3200px;width:317px;height:161px;background:#fff;font-size:16px;line-height:30px;color:#222;padding:42px 14px 0}
.rcard:after{content:"";position:absolute;left:40px;bottom:-18px;border:18px solid transparent;border-bottom:0;border-top-color:#fff}
.quote{width:66px;height:66px;border-radius:50%;background:#2f87d4;color:#fff;font-size:44px;text-align:center;line-height:78px;font-family:Georgia,serif}
.avatar{width:60px;height:60px;border-radius:50%;background:linear-gradient(180deg,#d9d9d9,#a9b4bf);border:3px solid #fff}
.rname{top:3410px;color:#fff;font-size:17px;line-height:27px}

/* footer */
.footer{left:0;top:3509px;width:1200px;height:271px;background:linear-gradient(90deg,#16345a,#1c3c66 50%,#213f68)}
.f-brand{left:100px;top:3556px;color:#fff;font-weight:700;font-size:26px;line-height:1}
.f-about{left:100px;top:3618px;width:238px;font-size:10px;line-height:14px;color:#dfe6ee}
.f-soc{top:3694px;width:9px;height:9px;border-radius:50%;background:#fff}
.f-col{top:3555px;color:#fff}
.f-col h4{font-size:12px;font-weight:600;letter-spacing:.3px;margin-bottom:14px}
.f-col li{list-style:none;font-size:10px;line-height:20px;padding-left:6px}
.f-col p{font-size:10px;line-height:14px;padding-left:2px;margin-bottom:26px}
.chat{left:1076px;top:3720px;width:124px;height:44px;background:#9acb3c;border-radius:22px 0 0 22px;color:#fff;font-size:9px;font-weight:700;text-align:right;padding:10px 8px 0 0;line-height:12px}
.chat i{position:absolute;left:0;top:-4px;width:50px;height:50px;border-radius:50%;background:#d7c3b5;border:3px solid #fff}
.copy{left:0;top:3780px;width:1200px;height:58px;background:var(--navy-dark);color:#fff;font-size:13px;text-align:center;line-height:58px}
</style>
</head>
<body>

<!-- header -->
<div class="abs brand">Bright Valley Goods<small>promos</small></div>
<div class="abs search">Search entire store here...
  <div class="abs search-btn"><svg width="38" height="38" viewBox="0 0 38 38"><circle cx="18" cy="18" r="6" fill="none" stroke="#fff" stroke-width="2.4"/><line x1="22.5" y1="22.5" x2="27" y2="27" stroke="#fff" stroke-width="2.6" stroke-linecap="round"/></svg></div>
</div>
<div class="abs cart"><svg width="24" height="22" viewBox="0 0 24 22"><path d="M1 2h4l3 12h11l3-9H7" fill="none" stroke="#111" stroke-width="2.2"/><circle cx="9" cy="18.5" r="2" fill="#111"/><circle cx="18" cy="18.5" r="2" fill="#111"/><circle cx="18" cy="4" r="4" fill="#2f87d4"/></svg>Cart</div>
<div class="abs phone-ico"><svg width="48" height="48" viewBox="0 0 48 48"><path d="M17 14c2-1 3 0 4 2l1 3c0 1-1 2-2 3 1 3 4 6 7 7 1-1 2-2 3-2l3 1c2 1 3 2 2 4-1 2-3 3-5 3-8-1-14-7-15-15 0-2 1-5 2-6z" fill="#fff"/></svg></div>
<div class="abs phone-txt">Call Us Toll Free:<br><b>1-800-555-0142</b></div>

<nav class="abs nav">
  <a class="active" style="left:319px">Home</a>
  <a style="left:428px">About Us</a>
  <a style="left:562px">Product</a>
  <a style="left:684px">Blog</a>
  <a style="left:772px">Contact Us</a>
</nav>

<!-- hero -->
<section class="abs hero">
  <div class="abs hero-photo" role="img" aria-label="Photo of a woman striding forward carrying printed tote bags"></div>
  <div class="abs hero-title display" style="left:89px;color:var(--green)">Bright Valley</div>
  <div class="abs hero-title display" style="left:721px;color:var(--red)">Goods</div>
</section>
<div class="abs rush">FREE<br>RUSH<span>Click Here</span></div>
<div class="abs dot" style="left:573px;top:683px;background:var(--green)"></div>
<div class="abs dot" style="left:594px;top:683px;background:var(--red)"></div>
<div class="abs dot" style="left:615px;top:683px;background:var(--red)"></div>

<!-- recommended -->
<h2 class="abs sec-title display" style="top:834px;font-weight:400">Recommended <span style="color:var(--navy)">Products</span></h2>

<div class="abs card" style="left:91px">
  <div class="abs img" role="img" aria-label="Purple and natural jute tote bags" style="background:linear-gradient(90deg,#5a3f9a 0 50%,#d6c08e 50%)"></div>
  <div class="abs stars">★★★★★</div><div class="abs name">Product Name</div><div class="abs price">$38.15</div>
  <div class="abs size">Size<span>16" W x 12" H x 6" D</span></div>
  <div class="abs cta">ADD TO CART</div>
  <div class="abs ico" style="left:156px"><svg width="30" height="30"><ellipse cx="15" cy="15" rx="7" ry="4.5" fill="none" stroke="#222" stroke-width="1.6"/><circle cx="15" cy="15" r="2" fill="#222"/></svg></div>
  <div class="abs ico" style="left:194px"><svg width="30" height="30"><circle cx="10" cy="15" r="2.4" fill="none" stroke="#222" stroke-width="1.4"/><circle cx="20" cy="10" r="2.4" fill="none" stroke="#222" stroke-width="1.4"/><circle cx="20" cy="20" r="2.4" fill="none" stroke="#222" stroke-width="1.4"/><path d="M12 14l6-3M12 16l6 3" stroke="#222" stroke-width="1.3"/></svg></div>
</div>
<div class="abs card" style="left:353px">
  <div class="abs img" role="img" aria-label="Blue and red printed tote bags" style="background:linear-gradient(90deg,#1f5fa8 0 50%,#d62a2f 50%)"></div>
  <svg class="abs" style="left:105px;top:70px" width="34" height="34"><circle cx="17" cy="17" r="16" fill="#fff"/><path d="M17 24l-7-7a4 4 0 0 1 7-4 4 4 0 0 1 7 4z" fill="#2f6fd4"/></svg>
  <div class="abs stars">★★★★★</div><div class="abs name">Product Name</div><div class="abs price">$12.17</div>
  <div class="abs size">Size<span>16" W x 12" H x 6" D</span></div>
  <div class="abs cta on">ADD TO CART</div>
  <div class="abs ico" style="left:156px"><svg width="30" height="30"><ellipse cx="15" cy="15" rx="7" ry="4.5" fill="none" stroke="#222" stroke-width="1.6"/><circle cx="15" cy="15" r="2" fill="#222"/></svg></div>
  <div class="abs ico" style="left:194px"><svg width="30" height="30"><circle cx="10" cy="15" r="2.4" fill="none" stroke="#222" stroke-width="1.4"/><circle cx="20" cy="10" r="2.4" fill="none" stroke="#222" stroke-width="1.4"/><circle cx="20" cy="20" r="2.4" fill="none" stroke="#222" stroke-width="1.4"/><path d="M12 14l6-3M12 16l6 3" stroke="#222" stroke-width="1.3"/></svg></div>
</div>
<div class="abs card" style="left:614px">
  <div class="abs img" role="img" aria-label="Green and natural printed tote bags" style="background:linear-gradient(90deg,#1e9a46 0 50%,#cdb58a 50%)"></div>
  <div class="abs ribbon" style="right:0;width:80px">New</div>
  <div class="abs stars">★★★★★</div><div class="abs name">Product Name</div><div class="abs price">$27.08</div>
  <div class="abs size">Size<span>16" W x 12" H x 6" D</span></div>
  <div class="abs cta">ADD TO CART</div>
  <div class="abs ico" style="left:156px"><svg width="30" height="30"><ellipse cx="15" cy="15" rx="7" ry="4.5" fill="none" stroke="#222" stroke-width="1.6"/><circle cx="15" cy="15" r="2" fill="#222"/></svg></div>
  <div class="abs ico" style="left:194px"><svg width="30" height="30"><circle cx="10" cy="15" r="2.4" fill="none" stroke="#222" stroke-width="1.4"/><circle cx="20" cy="10" r="2.4" fill="none" stroke="#222" stroke-width="1.4"/><circle cx="20" cy="20" r="2.4" fill="none" stroke="#222" stroke-width="1.4"/><path d="M12 14l6-3M12 16l6 3" stroke="#222" stroke-width="1.3"/></svg></div>
</div>
<div class="abs card" style="left:876px">
  <div class="abs img" role="img" aria-label="Red and jute printed tote bags" style="background:linear-gradient(90deg,#d8262c 0 50%,#b69a6c 50%)"></div>
  <div class="abs sale">SALE</div>
  <div class="abs stars">★★★★★</div><div class="abs name">Product Name</div><div class="abs price">$19.22</div>
  <div class="abs size">Size<span>16" W x 12" H x 6" D</span></div>
  <div class="abs cta">ADD TO CART</div>
  <div class="abs ico" style="left:156px"><svg width="30" height="30"><ellipse cx="15" cy="15" rx="7" ry="4.5" fill="none" stroke="#222" stroke-width="1.6"/><circle cx="15" cy="15" r="2" fill="#222"/></svg></div>
  <div class="abs ico" style="left:194px"><svg width="30" height="30"><circle cx="10" cy="15" r="2.4" fill="none" stroke="#222" stroke-width="1.4"/><circle cx="20" cy="10" r="2.4" fill="none" stroke="#222" stroke-width="1.4"/><circle cx="20" cy="20" r="2.4" fill="none" stroke="#222" stroke-width="1.4"/><path d="M12 14l6-3M12 16l6 3" stroke="#222" stroke-width="1.3"/></svg></div>
</div>
<div class="abs dot" style="left:573px;top:1330px;width:11px;height:11px;background:var(--navy)"></div>
<div class="abs dot" style="left:596px;top:1330px;width:11px;height:11px;background:var(--navy)"></div>
<div class="abs dot" style="left:619px;top:1330px;width:11px;height:11px;background:var(--navy)"></div>

<!-- banner -->
<section class="abs banner" role="img" aria-label="Photo of a woman jumping with a plain canvas tote bag against a pink wall">
  <div class="abs banner-person"></div>
</section>
<h2 class="abs display banner" style="background:none;width:auto;height:auto;top:1570px;left:524px;font-size:52px;font-weight:400"><span style="color:var(--navy)">New Bags</span> collection</h2>
<p class="abs banner-copy">Lorem ipsum dolor sit amet, consectetur adipiscing elit, sed do eiusmod tempor incididunt ut labore et dolore magna aliqua. Quis ipsum suspendisse ultrices gravida.</p>
<div class="abs btn-shop">SHOP NOW</div>

<!-- product detail -->
<div class="abs gallery"></div>
<div class="abs thumb" style="left:107px;top:2086px"><i style="background:#6cc644"></i></div>
<div class="abs thumb" style="left:107px;top:2187px"><i style="background:#157a46"></i></div>
<div class="abs thumb" style="left:107px;top:2295px"><i style="background:#20b5a6"></i></div>
<div class="abs thumb" style="left:474px;top:2086px"><i style="background:#1d1d1d"></i></div>
<div class="abs thumb" style="left:474px;top:2187px"><i style="background:#14402a"></i></div>
<div class="abs thumb" style="left:474px;top:2295px"><i style="background:#24288f"></i></div>
<div class="abs vline" style="left:201px"></div>
<div class="abs vline" style="left:457px"></div>
<div class="abs main-img" role="img" aria-label="Red and jute tote bags with printed imprint" style="left:215px;width:228px"></div>
<div class="abs size-line">Size:<b>13" W x 14" H x 7" D</b></div>

<div class="abs sku">SKU: PP2</div>
<div class="abs review"><span>★★★★★</span> &nbsp;|&nbsp; REVIEW</div>

<div class="abs ptable" style="top:2104px">
  <div class="head">IN-STOCK</div>
  <div class="row"><span>QTY</span><span>1</span><span>100+</span><span>250+</span><span>500+</span><span>1,000+</span><span>2,500+</span><span>5,000+</span></div>
  <div class="row"><span>PRICE</span><span>$0.69</span><span>$1.46</span><span>$1.35</span><span>$1.30</span><span>$1.26</span><span>$1.23</span><span>$1.19</span></div>
</div>
<div class="abs ptable" style="top:2238px">
  <div class="head">OVERSEAS</div>
  <div class="row"><span>QTY</span><span>1</span><span>1000+</span><span>3000+</span><span>5000+</span><span>1,0000+</span><span>2,5000+</span><span>5,0000+</span></div>
  <div class="row"><span>PRICE</span><span>$0.69</span><span>$1.44</span><span>$0.94</span><span>$1.30</span><span>$0.89</span><span>$0.74</span><span>$0.69</span></div>
</div>

<div class="abs pbtn" style="left:642px;width:160px;background:var(--green)">REQUEST A QUOTE</div>
<div class="abs pbtn" style="left:813px;width:115px;background:var(--navy)">BUY NOW</div>
<div class="abs pbtn" style="left:939px;width:161px;background:var(--green)">ORDER FREE SAMPLE</div>

<!-- production -->
<div class="abs prod" style="left:107px">
  <div class="head">In-stock Production<small>Order of 100Pcs or More</small></div>
  <div class="abs line" style="top:100px">Imprint Size<span>8" W * 8" H</span></div>
  <div class="abs line" style="top:154px">Additional Color<span>8" W * 8" H</span></div>
  <div class="abs line" style="top:209px">Full Color Imprint 300+<span>$1.00 each</span></div>
  <div class="abs line" style="top:261px;border-bottom:0">Set Up Free<span>$45. Per Color</span></div>
  <div class="abs foot">Order of 100Pcs or More</div>
</div>
<div class="abs prod" style="left:618px">
  <div class="head">Overseas Production<small>Free 1 Color, 2 Location Imprint</small></div>
  <div class="abs line" style="top:100px">Imprint Size<span>Unlimited</span></div>
  <div class="abs line" style="top:154px">Additional Color<span>$0.15 each</span></div>
  <div class="abs line" style="top:209px">Full Color Imprint 300+<span>Call</span></div>
  <div class="abs line" style="top:261px;border-bottom:0">Set Up Free<span>$45 Per Color</span></div>
  <div class="abs foot">Order of 1,000 Pcs More</div>
</div>

<!-- reviews -->
<section class="abs reviews"></section>
<h2 class="abs display" style="left:0;width:1200px;top:3080px;text-align:center;color:#fff;font-size:44px;font-weight:400">Customer Reviews</h2>

<div class="abs rcard" style="left:85px">“Lorem ipsum dolor sit amet, consectetur adipiscing elit, sed do eiusmod tempor incididunt ut labore et dolore.”</div>
<div class="abs rcard" style="left:437px">“Lorem ipsum dolor sit amet, consectetur adipiscing elit, sed do eiusmod tempor incididunt ut labore et dolore.”</div>
<div class="abs rcard" style="left:785px">“Lorem ipsum dolor sit amet, consectetur adipiscing elit, sed do eiusmod tempor incididunt ut labore et dolore.”</div>
<div class="abs quote" style="left:91px;top:3167px">“</div>
<div class="abs quote" style="left:444px;top:3167px">“</div>
<div class="abs quote" style="left:791px;top:3167px">“</div>
<svg class="abs" style="left:1122px;top:3236px" width="14" height="48"><circle cx="7" cy="6" r="5" fill="var(--navy)"/><circle cx="7" cy="24" r="5" fill="var(--navy)"/><circle cx="7" cy="42" r="5" fill="var(--navy)"/></svg>

<div class="abs avatar" role="img" aria-label="Customer portrait" style="left:104px;top:3403px"></div>
<div class="abs rname" style="left:182px">John S<br>Lorem ipsum dolor sit</div>
<div class="abs avatar" role="img" aria-label="Customer portrait" style="left:457px;top:3403px"></div>
<div class="abs rname" style="left:535px">David L<br>Lorem ipsum dolor sit</div>
<div class="abs avatar" role="img" aria-label="Customer portrait" style="left:804px;top:3403px"></div>
<div class="abs rname" style="left:882px">Kevin A<br>Lorem ipsum dolor sit</div>

<!-- footer -->
<footer class="abs footer" role="img" aria-label="Faint photo of stacked printed bags behind footer"></footer>
<div class="abs f-brand">Bright Valley<br><span style="font-size:18px">Goods</span></div>
<p class="abs f-about">Bright Valley Goods is an eco-friendly company that specializes in manufacturing custom bags. BVG was founded in 2009 and has strived to make the world a better place ever since.</p>
<div class="abs f-soc" style="left:100px"></div>
<div class="abs f-soc" style="left:115px"></div>
<div class="abs f-soc" style="left:130px"></div>
<div class="abs f-soc" style="left:145px"></div>
<div class="abs f-soc" style="left:160px"></div>

<div class="abs f-col" style="left:355px"><h4>USEFUL LINKS</h4><ul>
  <li>Customer Service</li><li>Our Story</li><li>Site Map</li><li>FTC Disclosure</li><li>Privacy Policy</li><li>Contact Us</li><li>Art &amp; Imprint Policy</li><li>Free Rush</li></ul></div>
<div class="abs f-col" style="left:609px"><h4>WHY BUY FROM US</h4><ul>
  <li>Reusable Bag Stats</li><li>Best Price Guarantee</li><li>Return &amp; Refund Policy</li><li>Shipping Policy</li><li>In-Stock &amp; Custom Production</li><li>Frequently Asked Questions</li></ul></div>
<div class="abs f-col" style="left:864px"><h4>ADDRESS</h4>
  <p style="margin-top:4px">48 Orchard Lane, Suite 7<br>Greenfield, OR 97000</p>
  <p>Phone: 1-800-555-0142</p>
  <p>Email: info@brightvalleygoods.example</p></div>

<div class="abs chat"><i role="img" aria-label="Support agent avatar"></i>LEAVE<br>A MESSAGE</div>
<div class="abs copy">Copyrights © 2020 Copyrights Company Name | All Rights Reserved</div>

</body>
</html>
```